New website for tarnova.se using wordpress

- Tarnova is a consultant broker based in Sweden
- Current web page: tarnova.se
- We want a new web page and we are aiming for simple and "clean"
- Two target groups:
1. Consultants/Consultant firms looking for assignments
2. Clients looking for consultants
- Colors + Logo attached

Requirements
Must have
• The new site should have separate pages the different sections. We have to be able to link to each page separately. NOT like the current web page where all the content is on one page.

```html
<!DOCTYPE html>
<html lang="en">
<head>
<meta charset="utf-8">
<title>Tarnova – Home page</title>
<link href="https://fonts.googleapis.com/css2?family=Montserrat:ital,wght@0,400;0,500;0,600;0,700;1,500&display=swap" rel="stylesheet">
<style>
:root{
  --purple:#6a329f;
  --purple-mid:#7b48ad;
  --purple-pale:#d9c8e9;
  --ink:#1c1c1c;
  --muted:#8a8a8a;
  --line:#555;
  --paper:#ffffff;
  --gray-band:#f7f7f7;
  --board:#f3f3f3;
  --footer:#000000;
}
*{box-sizing:border-box;margin:0;padding:0}
html,body{width:791px;height:1200px;overflow:hidden;background:var(--board);font-family:'Montserrat',sans-serif;color:var(--ink)}
.board{position:relative;width:791px;height:1200px}
.page{position:absolute;top:61px;width:507px;height:2136px;background:var(--paper);transform:scale(.5045);transform-origin:0 0;box-shadow:0 0 30px rgba(0,0,0,.12);overflow:hidden}
.page--color{left:93px}
.page--mono{left:442px}
.abs{position:absolute}
.eyebrow{color:var(--purple);font-size:8.5px;font-weight:500}
.h2{font-size:16px;font-weight:700;letter-spacing:.3px;text-transform:uppercase;line-height:20px}
.body{font-size:5.8px;line-height:10.8px;color:#777}
.btn{position:absolute;border:1px solid var(--line);font-size:6.5px;font-weight:500;text-transform:uppercase;display:flex;align-items:center;justify-content:center;letter-spacing:.3px;color:#333;white-space:nowrap}
.center{text-align:center}

/* photo areas */
.photo{position:absolute}
.page--color .ph-hero{background:linear-gradient(180deg,#3c4262 0%,#5b5674 18%,#9c6f86 34%,#e0947a 46%,#c9784e 58%,#8a5a3e 68%,#3b3234 78%,#2c3346 88%,#4b5262 100%)}
.page--mono .ph-hero{background:linear-gradient(180deg,#3a3a3a 0%,#6a6a6a 20%,#9c9c9c 40%,#b4b4b4 50%,#8c8c8c 62%,#4a4a4a 76%,#333 88%,#5a5a5a 100%)}
.page--color .ph-about{background:linear-gradient(120deg,#27333f 0%,#3d4a57 30%,#7d858c 55%,#d8d2cc 75%,#2e3540 100%)}
.page--mono .ph-about{background:linear-gradient(120deg,#2a2a2a 0%,#454545 30%,#858585 55%,#d4d4d4 75%,#333 100%)}
.page--color .ph-desk{background:linear-gradient(170deg,#f3f5f7 0%,#e2e7ec 40%,#c6ced6 62%,#8fbf9c 78%,#c9d0d6 100%)}
.page--mono .ph-desk{background:linear-gradient(170deg,#f2f2f2 0%,#e0e0e0 40%,#c4c4c4 62%,#8e8e8e 78%,#cfcfcf 100%)}
.ph-portrait{background:linear-gradient(180deg,#e4e4e4 0%,#c9c9c9 45%,#8e8e8e 75%,#4a4a4a 100%)}
.page--color .ph-news1{background:linear-gradient(160deg,#cfcfcf 0%,#6b6b6b 40%,#2b2b2b 75%,#4a4a4a 100%)}
.page--color .ph-news2{background:linear-gradient(160deg,#6fa8d8 0%,#b9d6ea 40%,#eae4da 70%,#8a8f96 100%)}
.page--color .ph-news3{background:linear-gradient(160deg,#e3ddd0 0%,#c3b59a 45%,#6f8a52 70%,#2f2f2f 100%)}
.page--mono .ph-news1{background:linear-gradient(160deg,#cfcfcf 0%,#6b6b6b 40%,#2b2b2b 75%,#4a4a4a 100%)}
.page--mono .ph-news2{background:linear-gradient(160deg,#b0b0b0 0%,#d6d6d6 40%,#e8e8e8 70%,#8c8c8c 100%)}
.page--mono .ph-news3{background:linear-gradient(160deg,#e0e0e0 0%,#b8b8b8 45%,#7a7a7a 70%,#2f2f2f 100%)}
.ph-badge{background:linear-gradient(135deg,#8a5cc0,#6a329f)}

/* hero */
.hero{position:absolute;left:0;top:0;width:507px;height:304px}
.logo-box{position:absolute;left:47px;top:0;width:71px;height:70px;background:var(--purple);display:flex;align-items:flex-end;justify-content:center;padding-bottom:10px}
.logo-word{color:#fff;font-weight:600;font-size:13px;letter-spacing:.5px}
.topline{position:absolute;right:47px;top:10px;display:flex;gap:8px;color:#fff;font-size:6.5px;align-items:center}
.topline span{display:flex;align-items:center;gap:4px}
.dot{width:12px;height:12px;border-radius:50%;background:#fff;display:inline-flex;align-items:center;justify-content:center}
.nav{position:absolute;right:47px;top:36px;display:flex;gap:14px;color:#fff;font-size:6.3px;font-weight:600;text-transform:uppercase}
.hero-kicker{position:absolute;top:86px;width:100%;text-align:center;color:#fff;font-size:17px;font-weight:500;line-height:20px}
.hero-title{position:absolute;top:110px;width:100%;text-align:center;color:#fff;font-size:25px;font-weight:700;letter-spacing:.5px;line-height:30px}
.hero .btn{left:217px;top:149px;width:74px;height:28px;border-color:rgba(255,255,255,.8);color:#fff}

/* audiences */
.bubble{position:absolute;top:262px;width:84px;height:84px;border-radius:50%;background:#fff;box-shadow:0 2px 8px rgba(0,0,0,.08);display:flex;align-items:center;justify-content:center}
.aud{position:absolute;top:357px;width:200px;text-align:center}
.aud .eyebrow{font-size:8px;line-height:10px}
.aud h3{font-size:10px;font-weight:600;margin-top:5px;line-height:12px}
.aud .body{margin-top:5px}

/* about */
.about{position:absolute;top:485px;left:0;width:507px;height:251px;background:var(--gray-band)}

/* solution */
.solution{position:absolute;top:736px;left:0;width:507px;height:242px}
.sol-panel{position:absolute;left:0;top:0;width:290px;height:242px;background:var(--purple-mid);color:#fff}
.sol-icon{position:absolute;left:47px;width:32px;height:32px;border-radius:50%;background:#fff;display:flex;align-items:center;justify-content:center}
.sol-text{position:absolute;left:86px;width:196px;font-size:6.3px;line-height:11px}

/* why */
.why{position:absolute;top:978px;left:0;width:507px;height:232px}
.venn{position:absolute;width:90px;height:90px;border-radius:50%}
.venn-icon{position:absolute;width:16px;height:16px;margin:-8px 0 0 -8px}
.venn-label{position:absolute;width:80px;margin-left:-40px;text-align:center;color:#fff;font-size:8.5px;font-weight:500;line-height:10px;margin-top:-5px}

/* team */
.team{position:absolute;top:1210px;left:0;width:507px;height:285px;background:var(--gray-band)}
.member{position:absolute;top:81px;width:120px;text-align:center}
.member .photo{position:static;width:120px;height:124px}
.member h4{font-size:9px;font-weight:600;margin-top:7px;line-height:11px}
.member .role{font-size:6.5px;font-style:italic;color:var(--muted);margin-top:2px}
.socials{display:flex;gap:3px;justify-content:center;margin-top:6px}
.soc{width:15px;height:15px;border-radius:50%;background:var(--purple);display:flex;align-items:center;justify-content:center}

/* testimonials */
.testimonials{position:absolute;top:1495px;left:0;width:507px;height:198px;background:linear-gradient(90deg,var(--purple),var(--purple-mid));color:#fff;text-align:center}
.quote-mark{position:absolute;left:72px;top:40px;font-size:70px;font-weight:700;color:rgba(255,255,255,.18);font-style:italic;line-height:1}
.quote{position:absolute;left:72px;top:71px;width:363px;font-size:9.5px;line-height:14px;font-style:italic;font-weight:500}
.quote-by{position:absolute;top:156px;width:100%;font-size:7.5px}

/* news */
.news{position:absolute;top:1693px;left:0;width:507px;height:282px}
.post{position:absolute;top:78px;width:131px}
.post .photo{position:static;width:131px;height:85px}
.post h5{font-size:7.8px;font-weight:600;line-height:10.5px;margin-top:12px;height:21px}
.post .by{font-size:6.3px;color:#666;margin-top:6px;display:flex;align-items:center;gap:2px}
.post .body{margin-top:7px;font-size:6.1px}

/* footer */
.footer{position:absolute;top:1975px;left:0;width:507px;height:161px;background:var(--footer);color:#fff}
.foot-logo{position:absolute;left:46px;top:0;width:113px;height:112px;background:var(--purple);display:flex;align-items:flex-end;justify-content:center;padding-bottom:16px}
.foot-logo .logo-word{font-size:21px}
.foot-col{position:absolute;top:20px}
.foot-col h6{font-size:7.5px;font-weight:600}
.foot-col ul{list-style:none;margin-top:11px;font-size:6.5px;line-height:12.7px}
.contact-row{display:flex;gap:5px;font-size:6.5px;line-height:12px;margin-top:8px;align-items:flex-start}
.contact-row .dot{flex:0 0 12px}
.foot-rule{position:absolute;left:47px;right:47px;top:128px;height:1px;background:#333}
.copy{position:absolute;left:47px;top:142px;font-size:6.5px}
.foot-soc{position:absolute;right:47px;top:138px;width:14px;height:14px;border-radius:50%;background:#fff}
</style>
</head>
<body>
<div class="board">

<!-- ===== Colour version ===== -->
<main class="page page--color">
  <section class="hero">
    <div class="photo ph-hero" style="inset:0" role="img" aria-label="Evening skyline of Stockholm old town across the water at sunset"></div>
    <div class="logo-box"><span class="logo-word">TARNOVA</span></div>
    <div class="topline">
      <span><i class="dot"><svg width="7" height="7" viewBox="0 0 24 24"><path fill="#333" d="M6.6 10.8a15 15 0 006.6 6.6l2.2-2.2a1 1 0 011-.25 11 11 0 003.6.6 1 1 0 011 1V20a1 1 0 01-1 1A17 17 0 013 4a1 1 0 011-1h3.5a1 1 0 011 1 11 11 0 00.6 3.6 1 1 0 01-.25 1z"/></svg></i>+46 (0) 8-555 010 20</span>
      <span><i class="dot"><svg width="7" height="7" viewBox="0 0 24 24"><path fill="#333" d="M2 5h20v14H2z"/><path fill="none" stroke="#fff" stroke-width="2" d="M2 6l10 7 10-7"/></svg></i>info@tarnova.se</span>
    </div>
    <nav class="nav"><span>Customer</span><span>About Tarnova</span><span>Consultants &amp; Partners</span><span>Contact</span></nav>
    <div class="hero-kicker">WE HELP YOURS</div>
    <h1 class="hero-title">BUSINESS TO GROW</h1>
    <a class="btn">Read more</a>
  </section>

  <div class="bubble" style="left:99px"><svg width="42" height="42" viewBox="0 0 42 42" fill="none" stroke="#6a329f" stroke-width="2.2"><circle cx="21" cy="15" r="8"/><path d="M7 38c1-9 7-13 14-13s13 4 14 13"/></svg></div>
  <div class="bubble" style="left:324px"><svg width="46" height="42" viewBox="0 0 46 42" fill="none" stroke="#6a329f" stroke-width="2"><circle cx="23" cy="20" r="6"/><path d="M12 38c1-7 5-10 11-10s10 3 11 10"/><path d="M23 3l1.4 2.8 3 .4-2.2 2.1.5 3-2.7-1.4-2.7 1.4.5-3-2.2-2.1 3-.4z"/><path d="M9 12l1.2 2.3 2.5.4-1.8 1.7.4 2.5L9 17.7 6.7 18.9l.4-2.5-1.8-1.7 2.5-.4z"/><path d="M37 12l1.2 2.3 2.5.4-1.8 1.7.4 2.5-2.3-1.2-2.3 1.2.4-2.5-1.8-1.7 2.5-.4z"/></svg></div>
  <div class="aud" style="left:41px"><div class="eyebrow">Consultants</div><h3>Looking for assignments</h3><p class="body">Duis aute irure dolor in reprehenderit in voluptate velit esse cillum dolore eu fugiat nulla pariatur.</p></div>
  <div class="aud" style="left:266px"><div class="eyebrow">Clients</div><h3>Looking for consultants</h3><p class="body">Duis aute irure dolor in reprehenderit in voluptate velit esse cillum dolore eu fugiat nulla pariatur.</p></div>
  <a class="btn" style="left:95px;top:425px;width:92px;height:25px">Register profile</a>
  <a class="btn" style="left:320px;top:425px;width:92px;height:25px">Register profile</a>

  <section class="about">
    <div class="photo ph-about" style="left:47px;top:30px;width:175px;height:180px" role="img" aria-label="Two businesswomen reviewing documents in an office"></div>
    <div class="photo ph-badge" style="left:160px;top:153px;width:77px;height:73px" role="img" aria-label="Illustration of a network of people under a magnifying glass"></div>
    <div class="abs eyebrow" style="left:250px;top:28px">About</div>
    <h2 class="abs h2" style="left:250px;top:44px">Welcome to Tarnova</h2>
    <p class="abs body" style="left:250px;top:74px;width:212px">Tarnova is part of Velmora, whose focus is on staffing and recruitment, while we at Tarnova focus on consulting brokerage services. We work professionally and personally and have broad experience in Finance, HR and IT. Our drive is to strengthen and supplement our customers' organizations with specialist knowledge in precisely these areas, including system development, project management, accounting, financial management and business development.</p>
    <a class="btn" style="left:250px;top:173px;width:69px;height:25px">Read more</a>
  </section>

  <section class="solution">
    <div class="sol-panel">
      <div class="abs" style="left:48px;top:24px;font-size:8.5px">Tarnova has</div>
      <h2 class="abs h2" style="left:48px;top:40px;color:#fff">The solution</h2>
      <i class="sol-icon" style="top:76px"><svg width="18" height="18" viewBox="0 0 24 24" fill="none" stroke="#333" stroke-width="1.6"><circle cx="12" cy="12" r="4"/><path d="M12 2v4M12 18v4M2 12h4M18 12h4M5 5l3 3M16 16l3 3M19 5l-3 3M8 16l-3 3"/></svg></i>
      <p class="sol-text" style="top:79px">We work with a smaller number of suppliers, which provides increased efficiency and simplifies work in your organization.</p>
      <i class="sol-icon" style="top:121px"><svg width="18" height="18" viewBox="0 0 24 24" fill="none" stroke="#333" stroke-width="1.6"><circle cx="12" cy="9" r="6"/><path d="M8 14l-2 8 6-3 6 3-2-8"/></svg></i>
      <p class="sol-text" style="top:124px">We ensure quality, make selections and manage negotiations and the administration of your assignments.</p>
      <i class="sol-icon" style="top:167px"><svg width="18" height="18" viewBox="0 0 24 24" fill="none" stroke="#333" stroke-width="1.6"><circle cx="12" cy="12" r="8"/><path d="M8 12l3 3 5-6"/></svg></i>
      <p class="sol-text" style="top:169px">We have recurring customer collaborations thanks to solid relationship building and personal service. A selection of returning customers: Region Norrvik, Brantbank, Telora, Skarp Group AB</p>
    </div>
    <div class="photo ph-desk" style="left:290px;top:0;width:217px;height:242px" role="img" aria-label="Hands writing notes next to a tablet showing a green bar chart"></div>
  </section>

  <section class="why">
    <div class="venn" style="left:108px;top:23px;background:var(--purple-pale)"></div>
    <div class="venn" style="left:63px;top:79px;background:rgba(165,130,200,.82)"></div>
    <div class="venn" style="left:137px;top:79px;background:rgba(123,72,173,.8)"></div>
    <svg class="venn-icon" style="left:153px;top:46px" viewBox="0 0 24 24" fill="none" stroke="#fff" stroke-width="3"><circle cx="10" cy="10" r="6"/><path d="M15 15l6 6"/></svg>
    <div class="venn-label" style="left:153px;top:68px">Transparency</div>
    <svg class="venn-icon" style="left:108px;top:114px" viewBox="0 0 24 24" fill="#fff"><circle cx="12" cy="7" r="5"/><path d="M3 22c0-6 4-9 9-9s9 3 9 9z"/></svg>
    <div class="venn-label" style="left:108px;top:141px">Personal</div>
    <svg class="venn-icon" style="left:192px;top:114px" viewBox="0 0 24 24" fill="none" stroke="#fff" stroke-width="2"><path d="M22 2L2 10l8 3 3 8z"/><path d="M22 2L10 13"/></svg>
    <div class="venn-label" style="left:192px;top:141px">Fast</div>
    <div class="abs eyebrow" style="left:261px;top:27px">Watchwords</div>
    <h2 class="abs h2" style="left:261px;top:44px">Why choose Tarnova?</h2>
    <p class="abs body" style="left:261px;top:74px;width:200px">As part of our team, you have access to interesting consulting assignments, committed and experienced project groups, which ensure quality, make selections, manage negotiation and follow-up and administration around your assignments. Our ambition is that it should be fun, developing and easy to get behind Tarnova, regardless of whether you are a one-person company or a larger consulting company.</p>
    <a class="btn" style="left:261px;top:177px;width:69px;height:25px">Read more</a>
  </section>

  <section class="team">
    <div class="abs eyebrow center" style="width:100%;top:28px">Team Tarnova</div>
    <h2 class="abs h2 center" style="width:100%;top:44px">We at Tarnova</h2>
    <div class="member" style="left:47px"><div class="photo ph-portrait" role="img" aria-label="Portrait of Linnea Morell"></div><h4>Linnea Morell</h4><div class="role">Delivery and Partner Manager</div><div class="socials"><i class="soc"></i><i class="soc"><svg width="8" height="6" viewBox="0 0 24 18"><rect width="24" height="18" fill="#fff"/><path d="M0 1l12 9 12-9" fill="none" stroke="#6a329f" stroke-width="2.5"/></svg></i></div></div>
    <div class="member" style="left:193px"><div class="photo ph-portrait" role="img" aria-label="Portrait of Sara Ekdahl"></div><h4>Sara Ekdahl</h4><div class="role">Delivery and Partner Manager</div><div class="socials"><i class="soc"></i><i class="soc"><svg width="8" height="6" viewBox="0 0 24 18"><rect width="24" height="18" fill="#fff"/><path d="M0 1l12 9 12-9" fill="none" stroke="#6a329f" stroke-width="2.5"/></svg></i></div></div>
    <div class="member" style="left:340px"><div class="photo ph-portrait" role="img" aria-label="Portrait of Maja Lindqvist"></div><h4>Maja Lindqvist</h4><div class="role">Delivery Coordinator</div><div class="socials"><i class="soc"></i><i class="soc"><svg width="8" height="6" viewBox="0 0 24 18"><rect width="24" height="18" fill="#fff"/><path d="M0 1l12 9 12-9" fill="none" stroke="#6a329f" stroke-width="2.5"/></svg></i></div></div>
  </section>

  <section class="testimonials">
    <div class="abs center" style="width:100%;top:20px;font-size:8.5px">Quote</div>
    <h2 class="abs h2 center" style="width:100%;top:35px;color:#fff">Testimonials</h2>
    <div class="quote-mark">“</div>
    <p class="quote">As a complement to our own agreements, we have chosen to cooperate with Tarnova. Tarnova helps us find assignments where we have full visibility into price and margins. We receive professional support throughout the process and can evaluate ourselves when and if the assignments suit our consultants.</p>
    <div class="quote-by">Johan Brevik, CEO, Nordkod AB</div>
  </section>

  <section class="news">
    <div class="abs eyebrow center" style="width:100%;top:24px">Our Post</div>
    <h2 class="abs h2 center" style="width:100%;top:40px">Latest news</h2>
    <article class="post" style="left:47px"><div class="photo ph-news1" role="img" aria-label="Row of parked cars"></div><h5>Extended collaboration with Vendel Cars</h5><div class="by">&#9679; Team Tarnova</div><p class="body">Tarnova further expands operations on the west coast through in-depth collaboration with Vendel Cars!</p></article>
    <article class="post" style="left:188px"><div class="photo ph-news2" role="img" aria-label="Man working at a desk in a bright office"></div><h5>We are expanding our expertise, now also in Finance and HR</h5><div class="by">&#9679; Team Tarnova</div><p class="body">We at Tarnova are now broadening our services further and helping with cutting-edge expertise...</p></article>
    <article class="post" style="left:330px"><div class="photo ph-news3" role="img" aria-label="Colleagues at a table with a laptop and plant"></div><h5>MSP (Managed Service Provider)</h5><div class="by">&#9679; Team Tarnova</div><p class="body">Tarnova supports you as a customer in all or part of the process to ensure that you always have the right skills ..</p></article>
  </section>

  <footer class="footer">
    <div class="foot-logo"><span class="logo-word">TARNOVA</span></div>
    <div class="foot-col" style="left:200px"><h6>Quick Links</h6><ul><li>Customer</li><li>About Tarnova</li><li>Consultants &amp; Partners</li><li>Contact</li></ul></div>
    <div class="foot-col" style="left:323px"><h6>Contact Information</h6>
      <div class="contact-row" style="margin-top:10px"><i class="dot"></i><span>Hamnvägen 12<br>116 30 Stockholm</span></div>
      <div class="contact-row"><i class="dot"></i><span>+46 (0) 8-555 010 20</span></div>
      <div class="contact-row"><i class="dot"></i><span>info@tarnova.se</span></div>
    </div>
    <div class="foot-rule"></div>
    <div class="copy">© Tarnova.se 2022 - Tarnova. All rights reserved.</div>
    <i class="foot-soc"></i>
  </footer>
</main>

<!-- ===== Monochrome photo version ===== -->
<main class="page page--mono">
  <section class="hero">
    <div class="photo ph-hero" style="inset:0" role="img" aria-label="Black and white skyline of Stockholm old town across the water"></div>
    <div class="logo-box"><span class="logo-word">TARNOVA</span></div>
    <div class="topline">
      <span><i class="dot"><svg width="7" height="7" viewBox="0 0 24 24"><path fill="#333" d="M6.6 10.8a15 15 0 006.6 6.6l2.2-2.2a1 1 0 011-.25 11 11 0 003.6.6 1 1 0 011 1V20a1 1 0 01-1 1A17 17 0 013 4a1 1 0 011-1h3.5a1 1 0 011 1 11 11 0 00.6 3.6 1 1 0 01-.25 1z"/></svg></i>+46 (0) 8-555 010 20</span>
      <span><i class="dot"><svg width="7" height="7" viewBox="0 0 24 24"><path fill="#333" d="M2 5h20v14H2z"/><path fill="none" stroke="#fff" stroke-width="2" d="M2 6l10 7 10-7"/></svg></i>info@tarnova.se</span>
    </div>
    <nav class="nav"><span>Customer</span><span>About Tarnova</span><span>Consultants &amp; Partners</span><span>Contact</span></nav>
    <div class="hero-kicker">WE HELP YOURS</div>
    <h1 class="hero-title">BUSINESS TO GROW</h1>
    <a class="btn">Read more</a>
  </section>

  <div class="bubble" style="left:99px"><svg width="42" height="42" viewBox="0 0 42 42" fill="none" stroke="#6a329f" stroke-width="2.2"><circle cx="21" cy="15" r="8"/><path d="M7 38c1-9 7-13 14-13s13 4 14 13"/></svg></div>
  <div class="bubble" style="left:324px"><svg width="46" height="42" viewBox="0 0 46 42" fill="none" stroke="#6a329f" stroke-width="2"><circle cx="23" cy="20" r="6"/><path d="M12 38c1-7 5-10 11-10s10 3 11 10"/><path d="M23 3l1.4 2.8 3 .4-2.2 2.1.5 3-2.7-1.4-2.7 1.4.5-3-2.2-2.1 3-.4z"/><path d="M9 12l1.2 2.3 2.5.4-1.8 1.7.4 2.5L9 17.7 6.7 18.9l.4-2.5-1.8-1.7 2.5-.4z"/><path d="M37 12l1.2 2.3 2.5.4-1.8 1.7.4 2.5-2.3-1.2-2.3 1.2.4-2.5-1.8-1.7 2.5-.4z"/></svg></div>
  <div class="aud" style="left:41px"><div class="eyebrow">Consultants</div><h3>Looking for assignments</h3><p class="body">Duis aute irure dolor in reprehenderit in voluptate velit esse cillum dolore eu fugiat nulla pariatur.</p></div>
  <div class="aud" style="left:266px"><div class="eyebrow">Clients</div><h3>Looking for consultants</h3><p class="body">Duis aute irure dolor in reprehenderit in voluptate velit esse cillum dolore eu fugiat nulla pariatur.</p></div>
  <a class="btn" style="left:95px;top:425px;width:92px;height:25px">Register profile</a>
  <a class="btn" style="left:320px;top:425px;width:92px;height:25px">Register profile</a>

  <section class="about">
    <div class="photo ph-about" style="left:47px;top:30px;width:175px;height:180px" role="img" aria-label="Two businesswomen reviewing documents in an office, black and white"></div>
    <div class="photo ph-badge" style="left:160px;top:153px;width:77px;height:73px" role="img" aria-label="Illustration of a network of people under a magnifying glass"></div>
    <div class="abs eyebrow" style="left:250px;top:28px">About</div>
    <h2 class="abs h2" style="left:250px;top:44px">Welcome to Tarnova</h2>
    <p class="abs body" style="left:250px;top:74px;width:212px">Tarnova is part of Velmora, whose focus is on staffing and recruitment, while we at Tarnova focus on consulting brokerage services. We work professionally and personally and have broad experience in Finance, HR and IT. Our drive is to strengthen and supplement our customers' organizations with specialist knowledge in precisely these areas, including system development, project management, accounting, financial management and business development.</p>
    <a class="btn" style="left:250px;top:173px;width:69px;height:25px">Read more</a>
  </section>

  <section class="solution">
    <div class="sol-panel">
      <div class="abs" style="left:48px;top:24px;font-size:8.5px">Tarnova has</div>
      <h2 class="abs h2" style="left:48px;top:40px;color:#fff">The solution</h2>
      <i class="sol-icon" style="top:76px"><svg width="18" height="18" viewBox="0 0 24 24" fill="none" stroke="#333" stroke-width="1.6"><circle cx="12" cy="12" r="4"/><path d="M12 2v4M12 18v4M2 12h4M18 12h4M5 5l3 3M16 16l3 3M19 5l-3 3M8 16l-3 3"/></svg></i>
      <p class="sol-text" style="top:79px">We work with a smaller number of suppliers, which provides increased efficiency and simplifies work in your organization.</p>
      <i class="sol-icon" style="top:121px"><svg width="18" height="18" viewBox="0 0 24 24" fill="none" stroke="#333" stroke-width="1.6"><circle cx="12" cy="9" r="6"/><path d="M8 14l-2 8 6-3 6 3-2-8"/></svg></i>
      <p class="sol-text" style="top:124px">We ensure quality, make selections and manage negotiations and the administration of your assignments.</p>
      <i class="sol-icon" style="top:167px"><svg width="18" height="18" viewBox="0 0 24 24" fill="none" stroke="#333" stroke-width="1.6"><circle cx="12" cy="12" r="8"/><path d="M8 12l3 3 5-6"/></svg></i>
      <p class="sol-text" style="top:169px">We have recurring customer collaborations thanks to solid relationship building and personal service. A selection of returning customers: Region Norrvik, Brantbank, Telora, Skarp Group AB</p>
    </div>
    <div class="photo ph-desk" style="left:290px;top:0;width:217px;height:242px" role="img" aria-label="Hands writing notes next to a tablet showing a bar chart, black and white"></div>
  </section>

  <section class="why">
    <div class="venn" style="left:108px;top:23px;background:var(--purple-pale)"></div>
    <div class="venn" style="left:63px;top:79px;background:rgba(165,130,200,.82)"></div>
    <div class="venn" style="left:137px;top:79px;background:rgba(123,72,173,.8)"></div>
    <svg class="venn-icon" style="left:153px;top:46px" viewBox="0 0 24 24" fill="none" stroke="#fff" stroke-width="3"><circle cx="10" cy="10" r="6"/><path d="M15 15l6 6"/></svg>
    <div class="venn-label" style="left:153px;top:68px">Transparency</div>
    <svg class="venn-icon" style="left:108px;top:114px" viewBox="0 0 24 24" fill="#fff"><circle cx="12" cy="7" r="5"/><path d="M3 22c0-6 4-9 9-9s9 3 9 9z"/></svg>
    <div class="venn-label" style="left:108px;top:141px">Personal</div>
    <svg class="venn-icon" style="left:192px;top:114px" viewBox="0 0 24 24" fill="none" stroke="#fff" stroke-width="2"><path d="M22 2L2 10l8 3 3 8z"/><path d="M22 2L10 13"/></svg>
    <div class="venn-label" style="left:192px;top:141px">Fast</div>
    <div class="abs eyebrow" style="left:261px;top:27px">Watchwords</div>
    <h2 class="abs h2" style="left:261px;top:44px">Why choose Tarnova?</h2>
    <p class="abs body" style="left:261px;top:74px;width:200px">As part of our team, you have access to interesting consulting assignments, committed and experienced project groups, which ensure quality, make selections, manage negotiation and follow-up and administration around your assignments. Our ambition is that it should be fun, developing and easy to get behind Tarnova, regardless of whether you are a one-person company or a larger consulting company.</p>
    <a class="btn" style="left:261px;top:177px;width:69px;height:25px">Read more</a>
  </section>

  <section class="team">
    <div class="abs eyebrow center" style="width:100%;top:28px">Team Tarnova</div>
    <h2 class="abs h2 center" style="width:100%;top:44px">We at Tarnova</h2>
    <div class="member" style="left:47px"><div class="photo ph-portrait" role="img" aria-label="Portrait of Linnea Morell"></div><h4>Linnea Morell</h4><div class="role">Delivery and Partner Manager</div><div class="socials"><i class="soc"></i><i class="soc"><svg width="8" height="6" viewBox="0 0 24 18"><rect width="24" height="18" fill="#fff"/><path d="M0 1l12 9 12-9" fill="none" stroke="#6a329f" stroke-width="2.5"/></svg></i></div></div>
    <div class="member" style="left:193px"><div class="photo ph-portrait" role="img" aria-label="Portrait of Sara Ekdahl"></div><h4>Sara Ekdahl</h4><div class="role">Delivery and Partner Manager</div><div class="socials"><i class="soc"></i><i class="soc"><svg width="8" height="6" viewBox="0 0 24 18"><rect width="24" height="18" fill="#fff"/><path d="M0 1l12 9 12-9" fill="none" stroke="#6a329f" stroke-width="2.5"/></svg></i></div></div>
    <div class="member" style="left:340px"><div class="photo ph-portrait" role="img" aria-label="Portrait of Maja Lindqvist"></div><h4>Maja Lindqvist</h4><div class="role">Delivery Coordinator</div><div class="socials"><i class="soc"></i><i class="soc"><svg width="8" height="6" viewBox="0 0 24 18"><rect width="24" height="18" fill="#fff"/><path d="M0 1l12 9 12-9" fill="none" stroke="#6a329f" stroke-width="2.5"/></svg></i></div></div>
  </section>

  <section class="testimonials">
    <div class="abs center" style="width:100%;top:20px;font-size:8.5px">Quote</div>
    <h2 class="abs h2 center" style="width:100%;top:35px;color:#fff">Testimonials</h2>
    <div class="quote-mark">“</div>
    <p class="quote">As a complement to our own agreements, we have chosen to cooperate with Tarnova. Tarnova helps us find assignments where we have full visibility into price and margins. We receive professional support throughout the process and can evaluate ourselves when and if the assignments suit our consultants.</p>
    <div class="quote-by">Johan Brevik, CEO, Nordkod AB</div>
  </section>

  <section class="news">
    <div class="abs eyebrow center" style="width:100%;top:24px">Our Post</div>
    <h2 class="abs h2 center" style="width:100%;top:40px">Latest news</h2>
    <article class="post" style="left:47px"><div class="photo ph-news1" role="img" aria-label="Row of parked cars"></div><h5>Extended collaboration with Vendel Cars</h5><div class="by">&#9679; Team Tarnova</div><p class="body">Tarnova further expands operations on the west coast through in-depth collaboration with Vendel Cars!</p></article>
    <article class="post" style="left:188px"><div class="photo ph-news2" role="img" aria-label="Man working at a desk in a bright office"></div><h5>We are expanding our expertise, now also in Finance and HR</h5><div class="by">&#9679; Team Tarnova</div><p class="body">We at Tarnova are now broadening our services further and helping with cutting-edge expertise...</p></article>
    <article class="post" style="left:330px"><div class="photo ph-news3" role="img" aria-label="Colleagues at a table with a laptop and plant"></div><h5>MSP (Managed Service Provider)</h5><div class="by">&#9679; Team Tarnova</div><p class="body">Tarnova supports you as a customer in all or part of the process to ensure that you always have the right skills ..</p></article>
  </section>

  <footer class="footer">
    <div class="foot-logo"><span class="logo-word">TARNOVA</span></div>
    <div class="foot-col" style="left:200px"><h6>Quick Links</h6><ul><li>Customer</li><li>About Tarnova</li><li>Consultants &amp; Partners</li><li>Contact</li></ul></div>
    <div class="foot-col" style="left:323px"><h6>Contact Information</h6>
      <div class="contact-row" style="margin-top:10px"><i class="dot"></i><span>Hamnvägen 12<br>116 30 Stockholm</span></div>
      <div class="contact-row"><i class="dot"></i><span>+46 (0) 8-555 010 20</span></div>
      <div class="contact-row"><i class="dot"></i><span>info@tarnova.se</span></div>
    </div>
    <div class="foot-rule"></div>
    <div class="copy">© Tarnova.se 2022 - Tarnova. All rights reserved.</div>
    <i class="foot-soc"></i>
  </footer>
</main>

</div>
</body>
</html>
```